Redesign of Business Cards to Update them!

We want a full overhaul of our business cards! We have a design that is almost 5 years old and it needs to be updated to be current

Address is 437 Dunmore Lane Suite C Marlow Springs CA 92517
PH: 9094718263
Zorlivo.com

Hours M-F 10AM-4PM
Sat and Sunday Closed

```html
<!DOCTYPE html>
<html lang="en">
<head>
<meta charset="utf-8">
<title>Zorlivo Business Cards</title>
<link href="https://fonts.googleapis.com/css2?family=Poppins:wght@400;600&display=swap" rel="stylesheet">
<style>
  :root {
    --brand-red: #ed1f27;
    --ink: #111111;
    --band-gray: #636363;
    --paper: #ffffff;
    --divider-gray: #c9c9c9;
    --divider-red: #f4b3b5;
  }
  html, body {
    margin: 0;
    padding: 0;
    width: 1200px;
    height: 1200px;
    overflow: hidden;
    background: var(--paper);
  }
  .canvas {
    position: relative;
    width: 1200px;
    height: 1200px;
    font-family: "Poppins", sans-serif;
    color: var(--ink);
  }
  .band { position: absolute; }
  .band-gray { left: 973px; top: 166px; width: 227px; height: 69px; background: var(--band-gray); }
  .band-red-left { left: 0; top: 582px; width: 210px; height: 24px; background: var(--brand-red); }
  .band-red-corner { position: absolute; left: 0; top: 0; width: 1200px; height: 1200px; }

  .card {
    position: absolute;
    width: 771px;
    height: 441px;
    box-shadow: 3px 3px 4px rgba(0,0,0,0.45);
  }
  .card-front { left: 202px; top: 165px; background: var(--paper); overflow: hidden; }
  .card-back { left: 202px; top: 657px; width: 774px; height: 442px; background: var(--brand-red); }

  .footer-strip { position: absolute; left: 0; bottom: 0; width: 771px; height: 24px; }

  .divider { position: absolute; width: 1px; }
  .divider-gray { left: 335px; top: 95px; height: 213px; background: var(--divider-gray); }
  .divider-red { left: 323px; top: 116px; height: 214px; background: var(--divider-red); }

  .mascot-art {
    position: absolute;
    background: var(--brand-red);
    border-radius: 6px;
  }
  .card-front .mascot-art { left: 71px; top: 155px; width: 190px; height: 84px; }
  .card-back .mascot-art { left: 205px; top: 101px; width: 338px; height: 150px; background: #f5f5f5; opacity: 0.92; }

  .brand-name {
    position: absolute;
    font-weight: 600;
    white-space: nowrap;
    text-align: center;
  }
  .card-front .brand-name { left: 71px; top: 244px; width: 190px; font-size: 34px; line-height: 40px; color: var(--ink); }
  .card-back .brand-name { left: 205px; top: 262px; width: 338px; font-size: 64px; line-height: 80px; color: var(--paper); }

  .contact {
    position: absolute;
    left: 345px;
    width: 400px;
    text-align: center;
    white-space: nowrap;
  }
  .contact-name { top: 96px; font-size: 30px; line-height: 40px; letter-spacing: 1px; }
  .contact-role { top: 136px; font-size: 22px; line-height: 30px; letter-spacing: 6px; }
  .contact-phone { top: 194px; font-size: 24px; line-height: 32px; letter-spacing: 0.5px; }
  .contact-web { top: 231px; font-size: 24px; line-height: 32px; }
  .contact-address { top: 285px; font-size: 20.5px; line-height: 26px; letter-spacing: 0.5px; }
  .address-line-1 { display: inline-block; padding-left: 42px; }
  .pin-icon { position: absolute; left: 401px; top: 281px; width: 28px; height: 33px; }
</style>
</head>
<body>
<div class="canvas">
  <div class="band band-gray"></div>
  <div class="band band-red-left"></div>
  <svg class="band-red-corner" viewBox="0 0 1200 1200" aria-hidden="true">
    <polygon points="976,1083 1200,1083 1200,1200 960,1200 863,1099 976,1099" fill="var(--brand-red)"/>
  </svg>

  <section class="card card-front">
    <div class="mascot-art" role="img" aria-label="Mascot illustration: a sad character with a broken phone, an arrow, then a happy character with a fixed phone"></div>
    <div class="brand-name">Zorlivo</div>

    <div class="divider divider-red"></div>
    <div class="divider divider-gray"></div>

    <div class="contact contact-name">YOUR NAME</div>
    <div class="contact contact-role">OWNER</div>
    <div class="contact contact-phone">PH: 9094718263</div>
    <div class="contact contact-web">Zorlivo.com</div>
    <svg class="pin-icon" viewBox="0 0 28 33" aria-hidden="true">
      <path d="M14 1a10 10 0 0 0-10 10c0 7 10 17 10 17s10-10 10-17A10 10 0 0 0 14 1z" fill="var(--brand-red)"/>
      <circle cx="14" cy="10.5" r="4.5" fill="var(--paper)"/>
      <ellipse cx="14" cy="30.5" rx="11" ry="2.3" fill="var(--ink)"/>
    </svg>
    <div class="contact contact-address">
      <span class="address-line-1">437 Dunmore Lane</span><br>
      Suite C Marlow Springs CA 92517
    </div>

    <svg class="footer-strip" viewBox="0 0 771 24" aria-hidden="true">
      <polygon points="0,0 385,0 373,24 0,24" fill="var(--brand-red)"/>
      <polygon points="397,0 771,0 771,24 385,24" fill="var(--ink)"/>
    </svg>
  </section>

  <section class="card card-back">
    <div class="mascot-art" role="img" aria-label="Mascot illustration in white: a sad character with a broken phone, an arrow, then a happy character with a fixed phone"></div>
    <div class="brand-name">Zorlivo</div>
  </section>
</div>
</body>
</html>
```